We need original design for our company business card, letterhead, invoice. Attached you can find our logo. We work in world fish trading and we are strongly oriented to technology.

```html
<!DOCTYPE html>
<html lang="en">
<head>
<meta charset="utf-8">
<title>Nerida – Business Card</title>
<link href="https://fonts.googleapis.com/css2?family=Open+Sans:wght@400;600;700&display=swap" rel="stylesheet">
<style>
  :root {
    --page: #e9e7e3;
    --card: #ffffff;
    --navy: #1d3557;
    --blue: #2a8fd8;
    --text: #2b2b2b;
    --muted: #7a7a7a;
    --rule: #c9c9c9;
    --green: #3f9a3a;
    --orange: #f4a21f;
  }
  * { box-sizing: border-box; margin: 0; padding: 0; }
  html, body { width: 1200px; height: 900px; overflow: hidden; }
  body {
    background: var(--page);
    font-family: "Open Sans", Arial, sans-serif;
    color: var(--text);
    position: relative;
  }
  .card {
    position: absolute;
    left: 280px;
    width: 640px;
    height: 366px;
    background: var(--card);
    box-shadow: 0 6px 18px rgba(0,0,0,.18);
    overflow: hidden;
  }
  .card-back { top: 40px; }
  .card-front { top: 494px; }

  .brand { display: flex; align-items: center; gap: 10px; }
  .brand-mark { width: 18px; height: 18px; border-radius: 50%; background: var(--green); }
  .brand-name { font-size: 38px; font-weight: 700; color: var(--navy); line-height: 1; }
  .tagline { font-size: 11px; color: var(--muted); margin-top: 5px; letter-spacing: .3px; }

  .card-back .brand-block { position: absolute; left: 0; right: 0; top: 120px; display: flex; flex-direction: column; align-items: center; }
  .card-back .web { position: absolute; left: 0; right: 0; top: 245px; text-align: center; font-size: 12px; font-weight: 600; color: var(--navy); }

  .card-front .bands { position: absolute; inset: 0; }
  .card-front .brand-block { position: absolute; right: 110px; top: 34px; text-align: right; }
  .card-front .brand { justify-content: flex-end; }
  .card-front .brand-rule { position: absolute; right: 90px; top: 112px; width: 250px; border-top: 1px solid var(--rule); }
  .address { position: absolute; right: 96px; top: 122px; text-align: right; font-size: 12.5px; line-height: 1.35; color: var(--text); font-style: normal; }

  .person { position: absolute; left: 40px; top: 190px; font-size: 19px; font-weight: 700; color: var(--navy); }
  .person .role { font-size: 13px; font-weight: 400; color: var(--muted); }
  .person .sep { font-weight: 400; color: var(--navy); margin: 0 4px; }
  .person-rule { position: absolute; left: 40px; top: 220px; width: 330px; border-top: 1px solid var(--rule); }

  .contacts { position: absolute; left: 44px; top: 226px; list-style: none; font-size: 13px; line-height: 18px; }
  .contacts li { display: flex; align-items: center; gap: 12px; }
  .contacts svg { width: 12px; height: 12px; fill: var(--muted); }

  .social { position: absolute; left: 40px; top: 340px; display: flex; align-items: center; gap: 10px; font-size: 13px; color: #fff; }
  .social-box { width: 13px; height: 13px; background: var(--navy); }
</style>
</head>
<body>

<section class="card card-back">
  <div class="brand-block">
    <div class="brand"><span class="brand-mark"></span><span class="brand-name">Nerida</span></div>
    <div class="tagline">seafood trading worldwide</div>
  </div>
  <div class="web">www.nerida-trade.com</div>
</section>

<section class="card card-front">
  <svg class="bands" viewBox="0 0 640 366" aria-hidden="true">
    <path d="M640 30 C625 170 545 290 410 366 L640 366 Z" fill="var(--green)"/>
    <path d="M0 336 L360 336 C480 336 560 300 612 196 C590 300 520 350 470 366 L0 366 Z" fill="var(--orange)"/>
  </svg>

  <div class="brand-block">
    <div class="brand"><span class="brand-mark"></span><span class="brand-name">Nerida</span></div>
    <div class="tagline">seafood trading worldwide</div>
  </div>
  <div class="brand-rule"></div>
  <address class="address">
    Nerida Holdings, LLC<br>
    210 Harbor Road Suite 500<br>
    Portview, LA 70990
  </address>

  <div class="person">Daniel Reeve<span class="sep">|</span><span class="role">CEO</span></div>
  <div class="person-rule"></div>
  <ul class="contacts">
    <li><svg viewBox="0 0 12 12"><path d="M3 1 L5 3.5 L4 5 C5 7 6 8 7.5 8.5 L9 7.5 L11.5 9.5 L10 11.5 C5 11 1 7 0.5 2.5 Z"/></svg>5550 1420</li>
    <li><svg viewBox="0 0 12 12"><rect x="1" y="4" width="10" height="7" rx="1"/><rect x="3" y="1" width="6" height="4"/></svg>5550 1421</li>
    <li><svg viewBox="0 0 12 12"><path d="M0.5 2.5 H11.5 V10 H0.5 Z M1 3 L6 7 L11 3" stroke="#fff" stroke-width=".8"/></svg>info@nerida-trade.com</li>
    <li><svg viewBox="0 0 12 12"><circle cx="6" cy="6" r="5.5"/><path d="M0.5 6 H11.5 M6 .5 V11.5" stroke="#fff" stroke-width=".7"/></svg>www.nerida-trade.com</li>
  </ul>
  <div class="social"><span class="social-box"></span>/neridatrade</div>
</section>

</body>
</html>
```